Re-design of current business cards

We are updating our website with new colors and layout. Would like to re-design our business cards to co-ordinate. See attached pdf with new Brindlecraft website colors. We would also like to combine our 2 brands on the one business card. Attached is the new design for our Brindlecraft website, current business cards, which are one sided, brindlecraft logo in tiff, .ai for fonts. Brindlecraft logo font is Optimum, Quillmarsh website home page image, Quillmarsh brand statics for products which includes the logo for this brand.

Quillmarsh brand will stay the dark gray on the website. See attached statics for product and website home page.
Updates

The business cards will be 2 sided. Brindlecraft Brand on one side and Quillmarsh Brand on the other. The colors for Brindlecraft need to follow the color scheme of the brindlecraft website pdf I uploaded. The colors are a blue, lighter teal blue and white. Quillmarsh needs to follow the dark gray color on files uploaded

Target Market(s)

The trade and consumers

Industry/Entity Type

Home Furnishing

Contact Information for Business Card

We are updating our website with new colors and layout. Would like to re-design our business cards to co-ordinate. We would also like to combine our 2 brands onto 1 2 sided business cards.

Requirements
Must have
• Colors that match our new website, see attached image.
• RGB colors
• navy -#152842
• teal - 98aeb9
• The gray color used for Quillmarsh brands.
• ll logos and fonts should stay the same.

```html
<!DOCTYPE html>
<html lang="en">
<head>
<meta charset="utf-8">
<title>Brindlecraft / Quillmarsh Business Card</title>
<link rel="stylesheet" href="https://fonts.googleapis.com/css2?family=Belleza&family=Roboto+Condensed:wght@300&display=swap">
<style>
  :root {
    --stage: #5f6573;
    --navy: #152842;
    --gray: #555555;
    --white: #ffffff;
    --rule: rgba(255,255,255,0.35);
  }
  * { box-sizing: border-box; margin: 0; padding: 0; }
  html, body { width: 1200px; height: 1200px; overflow: hidden; }
  body {
    background: var(--stage);
    font-family: "Belleza", "Optima", sans-serif;
    color: var(--white);
    position: relative;
  }
  .card {
    position: absolute;
    top: 215px;
    width: 440px;
    height: 770px;
    border-radius: 28px;
    box-shadow: 0 30px 60px rgba(0,0,0,0.35);
  }
  .card--front {
    left: 90px;
    background: var(--navy);
    display: flex;
    flex-direction: column;
    align-items: center;
    text-align: center;
    padding-top: 70px;
  }
  .card--back {
    left: 670px;
    background: var(--gray);
  }
  .brand-dot {
    width: 54px; height: 54px;
    border-radius: 50%;
    background: var(--white);
  }
  .brand-name {
    font-size: 40px;
    letter-spacing: 1px;
    margin-top: 12px;
    line-height: 1;
  }
  .brand-url { font-size: 14px; letter-spacing: 1px; margin-top: 6px; }
  .person-name { font-size: 36px; margin-top: 70px; line-height: 1; }
  .person-title { font-size: 17px; margin-top: 8px; }
  .divider {
    width: 230px; height: 1px;
    margin: 22px 0 26px;
    background: linear-gradient(90deg, transparent, var(--rule), transparent);
  }
  .address { font-size: 18px; line-height: 1.4; font-style: normal; }
  .contact { margin-top: 30px; display: flex; flex-direction: column; align-items: center; }
  .contact-icon { width: 36px; height: 36px; }
  .contact-value { font-size: 20px; letter-spacing: 1px; margin-top: 10px; }
  .contact + .contact { margin-top: 28px; }

  .sub-brand {
    position: absolute;
    left: 36px; right: 36px;
    top: 330px;
  }
  .sub-brand-name {
    font-size: 58px;
    letter-spacing: -1px;
    line-height: 1;
    white-space: nowrap;
  }
  .sub-brand-by {
    font-size: 11px;
    letter-spacing: 0.5px;
    text-align: right;
    margin-top: -2px;
  }
  .sub-brand-tagline {
    font-family: "Roboto Condensed", "Arial Narrow", sans-serif;
    font-weight: 300;
    font-size: 28px;
    margin-top: 10px;
    padding-left: 24px;
    white-space: nowrap;
  }
</style>
</head>
<body>
  <section class="card card--front" aria-label="Brindlecraft side">
    <div class="brand-dot"></div>
    <div class="brand-name">BRINDLECRAFT</div>
    <div class="brand-url">www.brindlecraft.com</div>

    <div class="person-name">DANA WHITLOW</div>
    <div class="person-title">Graphics/ Photography Director</div>
    <div class="divider"></div>

    <address class="address">
      PO Box 412/1870 Maple Ridge Rd<br>Fairbrook, Ohio 4381
    </address>

    <div class="contact">
      <svg class="contact-icon" viewBox="0 0 36 36" aria-hidden="true">
        <circle cx="18" cy="18" r="16" fill="var(--white)"/>
        <circle cx="18" cy="18" r="13" fill="var(--navy)"/>
        <path d="M12.5 11.5c1-.8 2-.6 2.6.3l1.4 2.2c.4.7.2 1.5-.4 2l-1 .8c.8 1.8 2.2 3.3 4 4.2l.9-1c.5-.6 1.4-.7 2-.3l2.2 1.4c.9.6 1 1.7.2 2.6-1.5 1.6-3.6 1.6-5.7.4-2.5-1.4-4.6-3.6-6-6.1-1.1-2.1-1.2-4.9-.2-6.5z" fill="var(--white)"/>
      </svg>
      <div class="contact-value">555.210.4407</div>
    </div>

    <div class="contact">
      <svg class="contact-icon" viewBox="0 0 36 36" aria-hidden="true">
        <circle cx="18" cy="18" r="16" fill="var(--white)"/>
        <circle cx="18" cy="18" r="13" fill="var(--navy)"/>
        <rect x="13" y="10" width="10" height="5" fill="var(--white)"/>
        <rect x="10" y="15" width="16" height="8" rx="1.5" fill="var(--white)"/>
        <rect x="13" y="20" width="10" height="7" fill="var(--white)" stroke="var(--navy)" stroke-width="1.2"/>
      </svg>
      <div class="contact-value">555.210.4418</div>
    </div>

    <div class="contact">
      <svg class="contact-icon" viewBox="0 0 36 36" aria-hidden="true">
        <circle cx="18" cy="18" r="16" fill="var(--white)"/>
        <circle cx="18" cy="18" r="13" fill="var(--navy)"/>
        <rect x="10.5" y="12.5" width="15" height="11" rx="1" fill="var(--white)"/>
        <path d="M10.5 13l7.5 6 7.5-6" fill="none" stroke="var(--navy)" stroke-width="1.3"/>
      </svg>
      <div class="contact-value">dwhitlow@brindlecraft.com</div>
    </div>
  </section>

  <section class="card card--back" aria-label="Quillmarsh side">
    <div class="sub-brand">
      <div class="sub-brand-name">QUILLMARSH</div>
      <div class="sub-brand-by">by BRINDLECRAFT</div>
      <div class="sub-brand-tagline">Find the comfort in every room.</div>
    </div>
  </section>
</body>
</html>
```